DL Flyer Design

I need a DL flyer, double-sided designed for a Brisbane based outdoor group exercise/training company called Move Ahead! Move Ahead! provides group outdoor training, designed for the individual. It provides the support, motivation and one-on-one attention of personal training combined with the support of a group environment. The classes are fun, challenging and aim to develop confidence & fitness. Weight loss is not the focus, although it is a benefit.
Updates

Hi

I've just uploaded a high res version of the logo if you need.

Cheers
Tam

Target Market(s)

English speaking men & women aged 25 - 45, white-collar office jobs. Average-low level of fitness, not hugely 'fitness' oriented but want to improve quality of life, overall fitness, lose a bit of weight.

Computer and consumer literate. Live in suburban Brisbane, Australia.

Industry/Entity Type

Training

Requirements
Must have
• Double sided DL. Use of black, greens and white per attached photos. Use of 1300 572 914 (1300 RUN FAR) and website www.movaheadactive.com.au

Indicative copy and contents is posted in the comments section.

```html
<!DOCTYPE html>
<html lang="en">
<head>
<meta charset="utf-8">
<title>Move Ahead! Weekly Class Timetable</title>
<link rel="stylesheet" href="https://fonts.googleapis.com/css2?family=Arimo:wght@400;700&display=swap">
<style>
  :root {
    --lime: #9cc43f;
    --forest: #22a84d;
    --leaf: #8dc63f;
    --rule: #b9d98a;
    --white: #ffffff;
    --ink: #1a1a1a;
  }
  * { margin: 0; padding: 0; box-sizing: border-box; }
  html, body { width: 1200px; height: 2400px; overflow: hidden; }
  body {
    position: relative;
    background: var(--lime);
    font-family: "Arimo", Arial, sans-serif;
  }
  .timetable {
    position: absolute;
    border-collapse: collapse;
    table-layout: fixed;
    border: 4px solid var(--forest);
    font-weight: 700;
    text-align: center;
  }
  .timetable th, .timetable td {
    border-left: 2px solid var(--rule);
    vertical-align: middle;
    line-height: 1.05;
  }
  .timetable th:first-child, .timetable td:first-child { border-left: none; }
  .timetable thead th {
    background: var(--forest);
    color: var(--white);
    font-size: 38px;
  }
  .timetable .slot td {
    background: var(--white);
    color: var(--leaf);
    font-size: 38px;
  }
  .timetable .break td {
    background: var(--forest);
    color: var(--white);
    font-size: 34px;
  }
  .timetable .time { text-align: left; padding-left: 26px; }

  .timetable--early { left: 56px; top: 66px; width: 1064px; }
  .timetable--early thead tr { height: 134px; }
  .timetable--early thead th { padding-top: 28px; }
  .timetable--early .slot-am { height: 164px; }
  .timetable--early .break { height: 132px; }
  .timetable--early .slot-pm { height: 214px; }
  .timetable--early .slot-pm td { padding-top: 30px; }

  .timetable--late { left: 66px; top: 780px; width: 1030px; }
  .timetable--late thead tr { height: 94px; }
  .timetable--late thead th { padding-top: 8px; }
  .timetable--late .slot-am { height: 150px; }
  .timetable--late .break { height: 176px; }
  .timetable--late .slot-pm { height: 200px; }
  .timetable--late .time { padding-left: 38px; }
  .timetable--late .top { vertical-align: top; padding-top: 40px; }

  .hero-art {
    position: absolute;
    left: 60px; top: 1300px;
    width: 1140px; height: 730px;
    background: radial-gradient(ellipse at 65% 45%, rgba(255,255,255,0.28), rgba(255,255,255,0) 70%);
  }
  .footer {
    position: absolute;
    left: 0; top: 2030px;
    width: 1200px; height: 370px;
    background: var(--white);
  }
  .brand {
    position: absolute;
    left: 150px; top: 90px;
    display: flex; align-items: center; gap: 20px;
  }
  .brand-dot { width: 44px; height: 44px; border-radius: 50%; background: var(--forest); }
  .brand-name { font-size: 84px; font-weight: 700; color: var(--forest); }
  .call-line {
    position: absolute;
    left: 146px; top: 268px;
    font-size: 38px; font-weight: 700; color: var(--forest);
  }
</style>
</head>
<body>
  <table class="timetable timetable--early">
    <colgroup><col style="width:210px"><col style="width:288px"><col style="width:264px"><col></colgroup>
    <thead>
      <tr><th class="time">Time</th><th>Monday</th><th>Tuesday</th><th>Wednesday</th></tr>
    </thead>
    <tbody>
      <tr class="slot slot-am"><td class="time">6.00am</td><td>Cardio</td><td></td><td>Stress-<br>relief<br>(boxing!)</td></tr>
      <tr class="break"><td></td><td></td><td></td><td></td></tr>
      <tr class="slot slot-pm"><td class="time">6.00pm</td><td>Strength</td><td>Cardio</td><td>Strength</td></tr>
    </tbody>
  </table>

  <table class="timetable timetable--late">
    <colgroup><col style="width:234px"><col style="width:254px"><col style="width:262px"><col></colgroup>
    <thead>
      <tr><th class="time">Time</th><th>Thursday</th><th>Friday</th><th>Saturday</th></tr>
    </thead>
    <tbody>
      <tr class="slot slot-am"><td class="time">6.00am</td><td>Cardio</td><td>Stress-<br>relief<br>(boxing!)</td><td class="top">Mash-up</td></tr>
      <tr class="break"><td></td><td></td><td></td><td>One-on-One<br>sessions</td></tr>
      <tr class="slot slot-pm"><td class="time">6.00pm</td><td>Stress-<br>relief<br>(boxing!)</td><td></td><td></td></tr>
    </tbody>
  </table>

  <div class="hero-art" role="img" aria-label="Illustration of a leaping runner silhouette over flowing white wave lines"></div>

  <footer class="footer">
    <div class="brand">
      <span class="brand-dot"></span>
      <span class="brand-name">Move Ahead!</span>
    </div>
    <p class="call-line">Call now on 1300 RUN FAR (1300 572 914)</p>
  </footer>
</body>
</html>
```